Brilliant Design Needed For Stand Up Pouch - Drink Mix

We need a layout for our resealable stand-up pouch that holds our powered sports drink mix. Target audience is endurance athletes that enjoy marathon running, cycling, mountain biking, hiking and triathlon. Secondary audience are participants in team sports such soccer, lacrosse, football and basketball. Please review the attached project brief for full details. Thanks!

Target Market(s)

50/50 male/female, ages 20-50, USA, succesful, driven, educated. Active, healthy, athletic, outdoor lifestyle.

Industry/Entity Type

Fitness

Font styles to use
Sans Serif

Colors
33a6d7
3277b5
abd037

Requirements
Must have
• Please review the attached project brief for full details.
Nice to have
Should not have

```html
<!DOCTYPE html>
<html lang="en">
<head>
<meta charset="UTF-8">
<title>Kinetra Sport Formula – Hydration Drink Mix Pouch</title>
<link href="https://fonts.googleapis.com/css2?family=Archivo:wght@300;400;700;800&family=Teko:wght@500;600&display=swap" rel="stylesheet">
<style>
  :root {
    --bg: #ececec;
    --lime: #a2c840;
    --lime-deep: #8db737;
    --lime-soft: #b2d451;
    --navy: #1b2d3d;
    --navy-blue: #173f56;
    --brand-blue: #33a6d7;
    --brand-mid: #3277b5;
    --ink: #111;
    --white: #fff;
    --silver: #d9dde0;
    --muted: #c9cfd4;
  }
  * { margin: 0; padding: 0; box-sizing: border-box; }
  html, body { width: 1200px; height: 1200px; overflow: hidden; background: var(--bg); }
  body { font-family: "Archivo", Arial, sans-serif; position: relative; }

  .pouch {
    position: absolute; left: 250px; top: 110px;
    width: 700px; height: 980px;
    border-radius: 18px; overflow: hidden;
    background: var(--lime);
    box-shadow: 0 30px 60px rgba(0,0,0,.18);
  }
  .pouch-art { position: absolute; inset: 0; }

  .tag {
    position: absolute; left: 60px; top: 60px;
    background: var(--white); color: var(--ink);
    font-weight: 700; font-size: 19px; letter-spacing: .5px;
    padding: 9px 22px; border-radius: 18px 6px 6px 6px;
  }
  .product-title { position: absolute; left: 60px; top: 112px; color: var(--ink); }
  .product-title .title { font-weight: 800; font-size: 60px; line-height: 1; }
  .product-title .subtitle { font-weight: 300; font-size: 52px; line-height: 1.05; }
  .product-title .flavor { font-weight: 400; font-size: 25px; line-height: 1.25; margin-top: 8px; }

  .brand {
    position: absolute; left: 372px; top: 520px;
    display: flex; align-items: center; gap: 14px;
  }
  .brand-mark { width: 30px; height: 30px; background: var(--brand-mid); }
  .brand-name { font-weight: 800; font-size: 50px; color: var(--brand-blue); letter-spacing: 1px; }

  .system { position: absolute; left: 380px; top: 610px; color: var(--white); }
  .system .lead { font-weight: 700; font-size: 38px; line-height: 1; }
  .system .rest { font-weight: 300; font-size: 28px; line-height: 1.3; }

  .formula {
    position: absolute; left: 340px; top: 700px;
    font-family: "Teko", "Arial Narrow", sans-serif; font-weight: 600;
    color: var(--silver); line-height: .85; text-transform: uppercase;
  }
  .formula .sport { font-size: 96px; display: block; }
  .formula .word { font-size: 66px; display: block; }

  .duration {
    position: absolute; left: 562px; top: 790px;
    color: var(--lime); font-size: 17px; line-height: 1.25; white-space: nowrap;
  }
  .duration strong { font-weight: 700; font-size: 19px; }

  .net {
    position: absolute; left: 330px; top: 900px;
    color: var(--muted); font-weight: 300; font-size: 22px; line-height: 1.25;
  }
</style>
</head>
<body>
  <main class="pouch">
    <svg class="pouch-art" viewBox="0 0 700 980" width="700" height="980">
      <defs>
        <linearGradient id="navyFade" x1="0" y1="0" x2="0" y2="1">
          <stop offset="0" stop-color="#173f56"/>
          <stop offset="1" stop-color="#1b2d3d"/>
        </linearGradient>
      </defs>
      <path class="navy-field" d="M0,560 C200,430 450,400 700,410 L700,980 L320,980 C170,900 70,840 0,800 Z" fill="url(#navyFade)"/>
      <path class="swoosh" d="M0,660 C190,520 420,450 650,450 C430,475 230,560 0,740 Z" fill="#b2d451"/>
      <rect class="runner-figure" x="110" y="500" width="180" height="340" rx="40" fill="#8db737" role="img" aria-label="Silhouette of a runner's legs mid-stride"/>
    </svg>

    <div class="tag">HYDRATION BY DURATION</div>
    <div class="product-title">
      <div class="title">Hydration</div>
      <div class="subtitle">drink mix</div>
      <div class="flavor">Lemon-Lime<br>with other natural flavors</div>
    </div>

    <div class="brand">
      <span class="brand-mark"></span>
      <span class="brand-name">KINETRA</span>
    </div>

    <div class="system">
      <div class="lead">Advanced</div>
      <div class="rest">Hydration System</div>
    </div>

    <div class="formula">
      <span class="sport">Sport</span>
      <span class="word">Formula</span>
    </div>

    <div class="duration">Recommended<br>for workouts<br><strong>lasting 1 hour</strong></div>

    <div class="net">Makes 27, 12 fl oz Servings<br>NET WT. 15.5 OZ (440G)</div>
  </main>
</body>
</html>
```